Tarrowind High School Association Website New Design

We require a fresh new website design for the Tarrowind High School Old Boys Association. The association is a non-for-profit and as such we like the site to reflect the ethos.
We require a design that uses responsive design techniques, so to allow the site to shift between mobile, tablet and desktop spaces and maintain elements in the site.
We would like a landing/home page design, and also an inner news/article based design included.
We want the site to appeal to a broad market of both the old guard members but also to bring on board the new social savey younger members.
The site needs to have a modern take on a professional yet fresh and opulent/elegant look.
A site that we like influences from is http://www.quennaval-lodge.com/ we especially like the navigation look and feel.
The site needs to be clean and simple to find information and navigate and as such would like the site design elements to reflect this in its layout and element interplay.
This site will act as an information gateway for the member's, but also offer abilities to purchase memberships, get information on up coming events and purchase tickets to these events, and interact with the members on the site.
Hi All designers,
The client has now agreed to make the project funding guaranteed, so I hope to see some great designs from you.
Thanks
Sorry all, I hadn't uploaded the logo, has now been uploaded.
Hi all designers, please don't let the wireframe layout include restrict your design freedom on the page layout. We included this to give you a feel for the elements wanted in the site, but not to push you to have them all in that arrangement. Feel free to move around or remove parts of to make better use of the space.
Also this site is for ex-students who are members of an association linked to the school, and not for the school itself, so your designs need to lean towards a member, events and reunions type site design.
After a review today, client now requires that the sites Events need special consideration. Want to see in a prominent position on the landing page area a good area to showcase the upcoming events. Please take this into consideration in your future design layouts.
Hi All Designers, I appreciate all the new and current designs, and sorry a bit behind on the feedback, have been a bit swamped on my own workload, I will give feedback to you all, and will maybe look at an extension of the deadline if need be, as to also allow the clients to look over designs.
Thanks
Reason: Extending the project deadline to allow more feedback to be provider to all designers, to allow review by clients and the feedback through myself.
Reason: Client was un-available for comment, and want them to be able to give feedback to designers for last round updates.
Reason: Sorry all, client has been overseas, and will only be back next week, so need to extend the deadline to allow for client input next week.
Reason: Sorry client has be delayed overseas, so when be needing to work through the designs next week to allow full ability to give all designs due recognition.
Reason: Waiting for client to review designs.
Target Market(s)
Professionals from all varity of job types
Industry/Entity Type
Events
Requirements
Must have
- Please use the attached Logo in the design and look to use the current colour pallet as much as possible, but open to colour and pallet additions or amendments.
Must have a “hero” header image scroller for ability to showcase upcoming events and other items (Required for home/landing pages, could be amended or removed on inner pages).
Should look to follow the include wire frame layout concept as a good conception starting point - but do not limit to just this layout, use design discretion.
Include prominently positioned events area in layout for upcoming events to push the events heavy aspect of the site.
Should include icons/link abilities to access social sites and applications. Ie Plumvine etc.
Nice to have
- A modern look with an edge to it.
Creative use of the sites colour pallet and site elements.
Should not have
- should not be a copy of the wireframe with colour added

```html
<!DOCTYPE html>
<html lang="en">
<head>
<meta charset="utf-8">
<title>Tarrowind – Home</title>
<link href="https://fonts.googleapis.com/css2?family=PT+Sans:wght@400;700&display=swap" rel="stylesheet">
<style>
:root{
  --green:#1b5e3b;
  --green-dark:#0c3a23;
  --green-mid:#17553a;
  --ink:#333;
  --muted:#555;
  --rule:#d6d6d6;
  --band:#efefef;
  --frame:#fff;
}
*{box-sizing:border-box;margin:0;padding:0}
html,body{width:800px;height:1200px;overflow:hidden}
body{position:relative;background:#fff;font-family:"PT Sans",sans-serif;color:var(--ink)}
a{color:inherit;text-decoration:none}
.abs{position:absolute}
.top-rule{left:0;top:0;width:800px;height:3px;background:#111}
.utility{right:48px;top:10px;font-size:8.5px;color:#444}
.utility span{margin:0 4px;color:#888}
.brand{left:38px;top:38px;font-size:27px;color:#333}
.search{left:567px;top:43px;width:186px;height:23px;border-radius:4px;background:linear-gradient(#f6f6f6,#e4e4e4);border:1px solid #d4d4d4;box-shadow:0 3px 4px rgba(0,0,0,.12)}
.search span{position:absolute;left:10px;top:4px;font-size:10px;color:#666}
.search svg{position:absolute;right:8px;top:5px}
.main-nav{left:35px;top:88px;width:725px;height:40px;background:linear-gradient(var(--green-mid),var(--green-dark));display:flex;padding-left:97px}
.main-nav a{display:flex;align-items:center;justify-content:center;color:#fff;font-size:11.5px;letter-spacing:.3px;height:100%;border-right:1px solid rgba(255,255,255,.15)}
.main-nav a:last-child{border-right:none}
.hero{left:36px;top:130px;width:724px;height:324px;background:linear-gradient(180deg,#5b6a55 0%,#7f8a6e 18%,#5a3a26 45%,#2a1b14 70%,#7a4a2a 100%)}
.hero-shadow{left:110px;top:452px;width:580px;height:22px;background:radial-gradient(ellipse at 50% 0,rgba(0,0,0,.22),rgba(0,0,0,0) 70%)}
.hero .arrow{position:absolute;top:145px}
h1.welcome{left:35px;top:482px;font-size:18.5px;font-weight:400;color:var(--green)}
.intro{left:38px;top:511px;width:712px;font-size:8.3px;line-height:13.4px;color:#333}
.intro p+p{margin-top:13.4px}
.band{left:0;top:630px;width:800px;height:342px;background:linear-gradient(#f1f1f1,#fff 45%)}
.section-title{font-size:16.5px;font-weight:400;color:var(--green)}
.thumb{background:var(--frame);padding:3px;box-shadow:0 0 0 1px #ddd,0 1px 3px rgba(0,0,0,.15)}
.thumb div{width:100%;height:100%}
.event{width:124px}
.event .thumb{height:78px}
.event-name{font-size:11.5px;color:#333;margin-top:9px}
.event-more{font-size:9.5px;color:#222;margin-top:3px}
.event-more::after{content:"";display:inline-block;margin-left:4px;border-left:3px solid #222;border-top:3px solid transparent;border-bottom:3px solid transparent}
.gallery .thumb{position:absolute;width:82px;height:65px}
.btn{background:var(--green-dark);color:#fff;font-size:9px;border-radius:4px;display:flex;align-items:center;justify-content:center}
.footer-band{left:0;top:972px;width:800px;height:150px;background:linear-gradient(var(--band),#f7f7f7 80%,#fff)}
.footer-title{font-size:13px;color:#333}
.quick{left:37px;top:1021px;width:305px}
.quick .row{display:flex;height:20.5px;align-items:center;border-bottom:1px solid var(--rule);font-size:9px;color:#333}
.quick .row:last-child{border-bottom:none}
.quick .row span:nth-child(1){width:111px;padding-left:1px}
.quick .row span:nth-child(2){width:95px}
.social{display:flex;gap:6px}
.social span{width:26px;height:26px;border-radius:50%;background:linear-gradient(#fff,#dcdcdc);box-shadow:0 1px 2px rgba(0,0,0,.35);display:flex;align-items:center;justify-content:center;font-size:11px;font-weight:700;color:#444}
.email{left:381px;top:1059px;width:177px;height:22px;border-radius:4px;background:linear-gradient(#e4e4e4,#d7d7d7);font-size:9px;font-style:italic;color:#666;padding:6px 10px;box-shadow:0 3px 4px rgba(0,0,0,.1)}
.contact{left:600px;top:1018px;font-size:9px;line-height:15px;color:#333}
.contact .org{color:var(--green);font-weight:700;padding-left:3px}
.contact .line{display:flex;padding-left:3px}
.contact .line b{font-weight:400;width:33px}
.bottom-rule{left:32px;top:1155px;width:745px;height:1px;background:#ddd}
.copyright{left:37px;top:1170px;font-size:7.5px;color:#333}
</style>
</head>
<body>
<div class="abs top-rule"></div>
<nav class="abs utility"><a href="#">Member</a><span>|</span><a href="#">FAQ</a><span>|</span><a href="#">Sitemap</a><span>|</span><a href="#">Contact</a></nav>
<div class="abs brand">Tarrowind</div>
<div class="abs search"><span>Enter keyword</span>
  <svg width="14" height="14" viewBox="0 0 14 14"><circle cx="5.5" cy="5.5" r="4" fill="none" stroke="#888" stroke-width="1.6"/><line x1="8.5" y1="8.5" x2="13" y2="13" stroke="#888" stroke-width="2"/></svg>
</div>
<nav class="abs main-nav">
  <a href="#" style="width:66px">HOME</a><a href="#" style="width:70px">ABOUT</a><a href="#" style="width:66px">NEWS</a><a href="#" style="width:69px">EVENTS</a><a href="#" style="width:79px">PHOTOS</a><a href="#" style="width:103px">MEMBERSHIP</a><a href="#" style="width:78px">CONTACT</a>
</nav>
<div class="abs hero" role="img" aria-label="School jazz band performing with a conductor under a glass and steel roof">
  <svg class="arrow" style="left:14px" width="18" height="30" viewBox="0 0 18 30"><polyline points="15,3 4,15 15,27" fill="none" stroke="rgba(255,255,255,.45)" stroke-width="3"/></svg>
  <svg class="arrow" style="right:14px" width="18" height="30" viewBox="0 0 18 30"><polyline points="3,3 14,15 3,27" fill="none" stroke="rgba(255,255,255,.45)" stroke-width="3"/></svg>
</div>
<div class="abs hero-shadow"></div>

<h1 class="abs welcome">Welcome to Tarrowind Website Mainpage</h1>
<div class="abs intro">
  <p>E-Commerce is a major progress in technology that has changed the way in which the customers now purchase information, products and the services. It's the new way of providing an opportuni-ty to make your products and services available in the global market 24 hours a day through Internet<br>Brightmesh eSolutions is specialized in handling advanced web projects and the ongoing projects that require permanent maintenance and support .We like challenges and do complete these challenge with expertise we like solving questions that arises in such projects as these helps us to grow also.</p>
  <p>Static website are the which are usually been used and are benefited through the Professionals and Small Companies. The companies with fewer budgets can promote their products and services through the static website and gain a lot.</p>
</div>

<div class="abs band"></div>
<h2 class="abs section-title" style="left:35px;top:648px">Upcoming Events</h2>
<div class="abs" style="left:31px;top:804px;width:430px;height:1px;background:var(--rule)"></div>
<div class="abs" style="left:461px;top:666px;width:1px;height:252px;background:var(--rule)"></div>

<div class="abs event" style="left:35px;top:680px"><div class="thumb"><div role="img" aria-label="Marching band in blue uniforms" style="background:linear-gradient(#3a3f66,#7d86b0 50%,#c9c9d6)"></div></div><div class="event-name">Your Event Name</div><div class="event-more">learn more about event</div></div>
<div class="abs event" style="left:174px;top:680px"><div class="thumb"><div role="img" aria-label="Colourful inflatable obstacle course in a hall" style="background:linear-gradient(135deg,#2a4ea8,#e8c21a 45%,#d9342b 75%,#3a3a6a)"></div></div><div class="event-name">Your Event Name</div><div class="event-more">learn more about event</div></div>
<div class="abs event" style="left:312px;top:680px"><div class="thumb"><div role="img" aria-label="Seminar audience facing a projection screen" style="background:radial-gradient(circle at 50% 35%,#7fb88a 0 14%,#2d3b33 40%,#151c18)"></div></div><div class="event-name">Your Event Name</div><div class="event-more">learn more about event</div></div>
<div class="abs event" style="left:35px;top:816px"><div class="thumb"><div role="img" aria-label="Banquet hall set for a dinner event" style="background:radial-gradient(circle at 50% 35%,#8ab8c8 0 12%,#5a3a22 40%,#2a1a10)"></div></div><div class="event-name">Your Event Name</div><div class="event-more">learn more about event</div></div>
<div class="abs event" style="left:174px;top:816px"><div class="thumb"><div role="img" aria-label="Stage lit in purple for a gala event" style="background:linear-gradient(#2a2a7a,#b02a9a 50%,#3a1440)"></div></div><div class="event-name">Your Event Name</div><div class="event-more">learn more about event</div></div>
<div class="abs event" style="left:312px;top:816px"><div class="thumb"><div role="img" aria-label="Large crowd at an evening reunion" style="background:linear-gradient(#1f3a22,#6d8a48 45%,#d8d0b8)"></div></div><div class="event-name">Your Event Name</div><div class="event-more">learn more about event</div></div>

<h2 class="abs section-title" style="left:480px;top:648px">Photo Gallery</h2>
<div class="abs gallery" style="left:0;top:0">
  <div class="thumb" style="left:482px;top:683px"><div role="img" aria-label="Students at classroom desks" style="background:linear-gradient(#7a8a6a,#c8b8a0 60%,#5a6a4a)"></div></div>
  <div class="thumb" style="left:577px;top:683px"><div role="img" aria-label="Young students in uniform raising hands" style="background:linear-gradient(#c98a6a,#3a6ad0 60%,#e6e6f0)"></div></div>
  <div class="thumb" style="left:671px;top:683px"><div role="img" aria-label="Graduates in red gowns" style="background:linear-gradient(#6a1a1a,#c8282a 55%,#8a1818)"></div></div>
  <div class="thumb" style="left:482px;top:762px"><div role="img" aria-label="Students working at tables" style="background:linear-gradient(#b8b0a0,#3a4a6a 60%,#8a7a6a)"></div></div>
  <div class="thumb" style="left:577px;top:762px"><div role="img" aria-label="Student reading a book" style="background:linear-gradient(135deg,#3a2418,#8a5a3a 50%,#d8c8a8)"></div></div>
  <div class="thumb" style="left:671px;top:762px"><div role="img" aria-label="Graduates tossing blue caps" style="background:linear-gradient(#b8c8e8,#2a2a8a 55%,#1a1a4a)"></div></div>
  <div class="thumb" style="left:482px;top:840px"><div role="img" aria-label="Graduates in black gowns celebrating" style="background:linear-gradient(#2a2a2a,#6a6a6a 50%,#1a1a1a)"></div></div>
  <div class="thumb" style="left:577px;top:840px"><div role="img" aria-label="Teacher helping children in class" style="background:linear-gradient(#d8d0c0,#9a7a6a 55%,#e6e0d8)"></div></div>
  <div class="thumb" style="left:671px;top:840px"><div role="img" aria-label="Student writing at a desk" style="background:linear-gradient(#e8e4dc,#c8b49a 55%,#f2efe8)"></div></div>
</div>
<div class="abs" style="left:480px;top:918px;width:275px;height:1px;background:var(--green)"></div>
<a class="abs btn" href="#" style="left:701px;top:929px;width:56px;height:22px">View more</a>

<div class="abs footer-band"></div>
<h3 class="abs footer-title" style="left:37px;top:992px;font-weight:400">Quick Links</h3>
<div class="abs quick">
  <div class="row"><span>Home</span><span>Membership</span><span>Resources</span></div>
  <div class="row"><span>About Our School</span><span>Education</span><span>Sitemap</span></div>
  <div class="row"><span>Gallery</span><span>Recent Blog</span><span>FAQ</span></div>
  <div class="row"><span>Testimonials</span><span>Results</span><span>Support</span></div>
  <div class="row"><span>Upcoming Events</span><span>Branches</span><span>Contact Information</span></div>
</div>

<h3 class="abs footer-title" style="left:381px;top:992px;font-weight:400">Connect With Us</h3>
<div class="abs social" style="left:379px;top:1019px">
  <span aria-label="Plumvine">P</span><span aria-label="Chirply">C</span><span aria-label="Linkwell">L</span>
</div>
<div class="abs email">email address here</div>
<a class="abs btn" href="#" style="left:504px;top:1087px;width:54px;height:21px">JOIN NOW</a>

<h3 class="abs footer-title" style="left:600px;top:992px;font-weight:400">Contact Information</h3>
<div class="abs contact">
  <div class="org">Tarrowind High School</div>
  <div class="line">Address: B17 Ferncliff Park Building Orlen US</div>
  <div class="line"><b>Ph:</b>(03) 9471 2086</div>
  <div class="line"><b>Fax:</b>585-774-312</div>
  <div class="line"><b>Email:</b>office@tarrowind.example</div>
</div>

<div class="abs bottom-rule"></div>
<div class="abs copyright">© 2012 Company Name &nbsp;|&nbsp; All right reserved &nbsp;|&nbsp; Term &amp; Conditions</div>
</body>
</html>
```